Innovative Freezer Label Design

Create a versatile and innovative freezer label design with universal appeal, suitable for different functionalities. The design should cater to a diverse audience, including those who freeze meals for meal prepping, batch cooking, and the restaurant industry. Our vision is a visually striking and distinctive design that embodies simplicity.

Example "our current labels feature essential details like "Contents" and "Date." We recognize these as crucial points of information. Currently, the challenge lies in creating various labels for different marketplaces, considering language barriers. A proposed solution involves the integration of universal icons to replace specific words, promoting practicality for international sales."

Kindly note that design concepts should not be restricted to our current product, brand guideline, logo, or the provided example.

Our goal is not only product differentiation but also increased sales through a blend of functionality and aesthetics.

The following are examples of freezer labels designs. Kindly do not restrict your designs to the examples. The designs must be universal (for language barrier purposes)

Examples:
https://www.tackvora.co.uk/pin/5827164039281736401/
https://www.tackvora.co.uk/pin/5827164039281736405/
https://www.tackvora.co.uk/pin/5827164039281736394/
https://www.tackvora.co.uk/pin/5827164039281736308/
https://www.tackvora.co.uk/pin/5827164039281797750/

Please reach out if you have any questions.

Thank you

```html
<!DOCTYPE html>
<html lang="en">
<head>
<meta charset="utf-8">
<title>Freezer Label – Nordel</title>
<link href="https://fonts.googleapis.com/css2?family=Open+Sans:wght@400;600&display=swap" rel="stylesheet">
<style>
  :root {
    --page-bg: #ffffff;
    --label-bg: #ffffff;
    --ink: #3b4853;
    --tab: #46545e;
    --tab-ink: #ffffff;
    --rule: #3b4853;
    --dash: #9aa3aa;
  }
  * { box-sizing: border-box; margin: 0; padding: 0; }
  html, body {
    width: 1200px;
    height: 621px;
    overflow: hidden;
    background: var(--page-bg);
    font-family: "Open Sans", Arial, sans-serif;
    color: var(--ink);
  }
  .canvas { position: relative; width: 1200px; height: 621px; }

  .freezer-label {
    position: absolute;
    left: 440px;
    top: 21px;
    width: 420px;
    height: 760px;
    transform: scale(0.76);
    transform-origin: top left;
    background: var(--label-bg);
    border: 2px solid var(--ink);
    border-radius: 46px;
    overflow: hidden;
    box-shadow: 0 4px 6px rgba(0,0,0,0.12);
  }

  .month-list {
    position: absolute;
    left: 34px;
    top: 50px;
    list-style: none;
    font-size: 25px;
    line-height: 41.7px;
  }
  .month-divider {
    position: absolute;
    left: 90px;
    top: 64px;
    width: 2px;
    height: 468px;
    background: var(--rule);
  }

  .day-grid {
    position: absolute;
    left: 128px;
    top: 50px;
    display: grid;
    grid-template-columns: repeat(5, 48.5px);
    grid-auto-rows: 46px;
    font-size: 24px;
    text-align: center;
    align-items: center;
  }

  .contents-field {
    position: absolute;
    left: 137px;
    top: 383px;
    display: flex;
    align-items: center;
    font-size: 28px;
  }
  .contents-field .underline {
    width: 110px;
    height: 2px;
    background: var(--rule);
    margin-left: 8px;
    margin-top: 4px;
  }

  .write-line {
    position: absolute;
    left: 139px;
    width: 224px;
    border-top: 1.5px dashed var(--dash);
  }

  .brand-tab {
    position: absolute;
    left: 0;
    top: 562px;
    width: 107px;
    height: 200px;
    background: var(--tab);
    border-top-right-radius: 42px;
  }
  .brand-name {
    position: absolute;
    left: 53px;
    top: 100px;
    transform: translate(-50%, -50%) rotate(-90deg);
    color: var(--tab-ink);
    font-size: 30px;
    font-weight: 600;
    letter-spacing: 2px;
    white-space: nowrap;
  }
</style>
</head>
<body>
<main class="canvas">
  <section class="freezer-label" aria-label="Freezer label">
    <ul class="month-list">
      <li>Jan</li><li>Feb</li><li>Mar</li><li>Apr</li><li>May</li><li>Jun</li>
      <li>Jul</li><li>Aug</li><li>Sep</li><li>Oct</li><li>Nov</li><li>Dec</li>
    </ul>
    <div class="month-divider"></div>

    <div class="day-grid">
      <span>1</span><span>2</span><span>3</span><span>4</span><span>5</span>
      <span>6</span><span>7</span><span>8</span><span>9</span><span>10</span>
      <span>11</span><span>12</span><span>13</span><span>14</span><span>15</span>
      <span>16</span><span>17</span><span>18</span><span>19</span><span>20</span>
      <span>21</span><span>22</span><span>23</span><span>24</span><span>25</span>
      <span>26</span><span>27</span><span>28</span><span>29</span><span>30</span>
      <span>31</span>
    </div>

    <div class="contents-field"><span>Contens</span><span class="underline"></span></div>
    <div class="write-line" style="top:452px"></div>
    <div class="write-line" style="top:512px"></div>
    <div class="write-line" style="top:572px"></div>
    <div class="write-line" style="top:632px"></div>
    <div class="write-line" style="top:692px"></div>

    <div class="brand-tab">
      <span class="brand-name">NORDEL</span>
    </div>
  </section>
</main>
</body>
</html>
```